A clean crisp business card for a Landscape Construction company. Designed to be easy to read contact/ info and also be appealing/interesting, unlike a traditional business card.

Industry/Entity Type

Landscape Construction

Contact Information for Business Card

Company name : Bramblecrest Landscape Construction, phone number: (877) 62Vales, website:Bramblecrestlandscapes.example, Email, sales@bramblecrestlandscapes.example

Requirements
Nice to have
• Luxurious finishes/ details…. Icons or emblems next to contact info
Should not have
• Clipart or general pictures

```html
<!DOCTYPE html>
<html lang="en">
<head>
<meta charset="utf-8">
<title>Bramblecrest Landscape Construction – Business Card</title>
<link rel="stylesheet" href="https://fonts.googleapis.com/css2?family=Cinzel:wght@500;600&family=Open+Sans:wght@400;600&display=swap">
<style>
  :root {
    --canvas: #e4e5e4;
    --lime: #9bc53d;
    --lime-light: #addb4e;
    --royal: #1f6cc4;
    --royal-deep: #1258b3;
    --royal-light: #3a84d2;
    --white: #ffffff;
  }
  * { margin: 0; padding: 0; box-sizing: border-box; }
  html, body {
    width: 1200px; height: 675px; overflow: hidden;
    background: var(--canvas);
  }
  .canvas {
    position: relative; width: 1200px; height: 675px;
    display: flex; align-items: center; justify-content: center; gap: 50px;
  }
  .card {
    position: relative; width: 500px; height: 286px;
    border-radius: 18px;
    box-shadow: 0 8px 22px rgba(0,0,0,0.18);
    overflow: hidden;
  }
  /* Front: contact side */
  .card-front {
    background: linear-gradient(160deg, var(--lime) 0%, var(--lime-light) 100%);
  }
  .front-brand {
    position: absolute; left: 48px; top: 44px;
    display: flex; align-items: center; gap: 12px;
  }
  .brand-dot {
    width: 22px; height: 22px; border-radius: 50%;
    background: var(--royal);
  }
  .brand-name {
    font-family: "Cinzel", serif; font-weight: 600;
    color: var(--royal); line-height: 1.05;
  }
  .front-brand .brand-name { font-size: 30px; }
  .front-brand .brand-sub {
    display: block; font-size: 12.5px; letter-spacing: 3.2px; margin-top: 4px;
  }
  .divider {
    position: absolute; left: 34px; right: 86px; top: 140px;
    height: 0; border-top: 2px solid var(--royal);
    box-shadow: 0 -4px 0 -1px var(--white);
  }
  .contact-list {
    position: absolute; left: 40px; top: 160px;
    list-style: none;
    font-family: "Open Sans", sans-serif; font-size: 14.5px;
    color: var(--royal-deep);
  }
  .contact-list li {
    display: flex; align-items: center; gap: 9px; height: 25px;
  }
  .contact-icon { width: 17px; height: 17px; flex: none; }
  .holder {
    position: absolute; right: 44px; top: 196px; text-align: right;
  }
  .holder-name {
    font-family: "Cinzel", serif; font-weight: 600; font-size: 26px;
    color: var(--royal); letter-spacing: 1px; line-height: 1;
  }
  .holder-role {
    font-family: "Open Sans", sans-serif; font-size: 12.5px;
    color: var(--royal-deep); padding-bottom: 2px;
    border-bottom: 2px solid var(--royal); padding-left: 80px;
  }
  /* Back: brand side */
  .card-back {
    background: linear-gradient(135deg, var(--royal-deep) 0%, var(--royal) 45%, var(--royal-light) 100%);
    display: flex; align-items: center; justify-content: center;
  }
  .back-brand {
    display: flex; align-items: center; gap: 14px;
  }
  .back-brand .brand-dot { background: var(--white); width: 26px; height: 26px; }
  .back-brand .brand-name { color: var(--white); font-size: 34px; }
  .back-brand .brand-sub {
    display: block; font-size: 14px; letter-spacing: 3.6px; margin-top: 6px;
  }
</style>
</head>
<body>
<main class="canvas">

  <section class="card card-front" aria-label="Business card front">
    <div class="front-brand">
      <span class="brand-dot"></span>
      <p class="brand-name">Bramblecrest<span class="brand-sub">Landscape Construction</span></p>
    </div>

    <div class="divider"></div>

    <ul class="contact-list">
      <li>
        <svg class="contact-icon" viewBox="0 0 20 20" aria-hidden="true">
          <circle cx="10" cy="10" r="10" fill="var(--royal)"/>
          <path d="M6.5 5.5c.6-.4 1.2-.3 1.5.2l1 1.6c.2.4.1.9-.3 1.2l-.6.4c.5 1.2 1.4 2.1 2.6 2.6l.4-.6c.3-.4.8-.5 1.2-.3l1.6 1c.5.3.6.9.2 1.5-.6.9-1.6 1.2-2.6.8-2.4-1-4.2-2.8-5.2-5.2-.4-1 0-2 .2-2.2z" fill="var(--white)"/>
        </svg>
        <span>(877) 62Vales</span>
      </li>
      <li>
        <svg class="contact-icon" viewBox="0 0 20 20" aria-hidden="true">
          <circle cx="10" cy="10" r="10" fill="var(--royal)"/>
          <circle cx="10" cy="10" r="5" fill="none" stroke="var(--white)" stroke-width="1.2"/>
          <ellipse cx="10" cy="10" rx="2.2" ry="5" fill="none" stroke="var(--white)" stroke-width="1.1"/>
          <line x1="5" y1="10" x2="15" y2="10" stroke="var(--white)" stroke-width="1.1"/>
        </svg>
        <span>www.bramblecrestlandscapes.example</span>
      </li>
      <li>
        <svg class="contact-icon" viewBox="0 0 20 20" aria-hidden="true">
          <circle cx="10" cy="10" r="10" fill="var(--royal)"/>
          <rect x="5" y="6.5" width="10" height="7" rx="1" fill="var(--white)"/>
          <path d="M5.3 7l4.7 3.6L14.7 7" fill="none" stroke="var(--royal)" stroke-width="1.1"/>
        </svg>
        <span>sales@bramblecrestlandscapes.example</span>
      </li>
    </ul>

    <div class="holder">
      <p class="holder-name">NAME</p>
      <p class="holder-role">Owner</p>
    </div>
  </section>

  <section class="card card-back" aria-label="Business card back">
    <div class="back-brand">
      <span class="brand-dot"></span>
      <p class="brand-name">Bramblecrest<span class="brand-sub">Landscape Construction</span></p>
    </div>
  </section>

</main>
</body>
</html>
```